Brantley Water Taxi and Transport

Need to redesign our business cards to relay that we do freight logistics and water taxi service. We also work with gov. agencies doing environmental clean up, oil spill response, remote site construction and work with many of the air taxi and helicopter services on Kodiak Island. Out website is www.brantleywatertaxi-example.com to get a better idea of what we do.

Contact Information for Business Card

I have a previous business card but it just has the logo on the front, and a sunset picture on the back with the contact info. It does not relay what we do and what we can help with. I like a simple straight forward design over a busy one.

Colors
3176b5
0455a3
cfdfed

Requirements
Must have
• logo, email, website, phone number

```html
<!DOCTYPE html>
<html lang="en">
<head>
<meta charset="utf-8">
<title>Brantley Water Taxi and Transport – Business Card</title>
<link href="https://fonts.googleapis.com/css2?family=Roboto:wght@400;500;700&display=swap" rel="stylesheet">
<style>
  :root {
    --backdrop: #a6d6c3;
    --card-white: #ffffff;
    --brand-navy: #0a3fae;
    --brand-blue: #0455a3;
    --brand-mid: #3176b5;
    --sky-blue: #5ab4e0;
    --sunset-orange: #f7a21b;
    --pale-blue: #cfdfed;
  }
  * { margin: 0; padding: 0; box-sizing: border-box; }
  html, body {
    width: 1200px; height: 1199px; overflow: hidden;
    background: var(--backdrop);
    font-family: "Roboto", Arial, sans-serif;
  }
  .canvas { position: relative; width: 1200px; height: 1199px; }

  .card {
    position: absolute; left: 235px; width: 730px;
    border-radius: 41px; overflow: hidden;
  }
  .card-front { top: 167px; height: 417px; background: var(--card-white); }
  .card-back { top: 614px; height: 418px; }

  .emblem-area {
    position: absolute; left: 137px; top: 89px; width: 235px; height: 110px;
    border-radius: 8px;
    background: linear-gradient(180deg, #e9f5fb 0%, var(--pale-blue) 55%, #b9dcf0 100%);
  }
  .company-name {
    position: absolute; left: 384px; top: 113px; width: 300px;
    color: var(--brand-navy); font-weight: 700; font-size: 27px; line-height: 1.1;
  }
  .captain {
    position: absolute; left: 0; right: 0; top: 217px; text-align: center;
    color: var(--sky-blue); font-weight: 700; font-size: 27px;
  }
  .captain .rank { font-size: 20px; font-weight: 500; margin-right: 6px; }
  .contact-list {
    position: absolute; left: 257px; top: 258px; list-style: none;
  }
  .contact-list li {
    display: flex; align-items: center; gap: 5px; height: 24.5px;
    color: var(--brand-blue); font-weight: 700; font-size: 16px;
  }
  .contact-icon { width: 17px; height: 17px; flex: none; }
  .band-blue {
    position: absolute; left: 0; right: 0; top: 358px; height: 47px;
    background: var(--brand-blue);
  }
  .band-orange {
    position: absolute; left: 0; right: 0; top: 405px; height: 12px;
    background: var(--sunset-orange);
  }

  .back-photo {
    position: absolute; inset: 0;
    background: linear-gradient(160deg, #3f78b8 0%, #2a62a6 40%, #1d4f94 70%, #2b64a8 100%);
  }
  .back-name {
    position: absolute; left: 0; right: 0; top: 186px; text-align: center;
    color: var(--card-white); font-weight: 700; font-size: 30px;
  }
</style>
</head>
<body>
<main class="canvas">
  <section class="card card-front">
    <div class="emblem-area" role="img" aria-label="Illustration of a work boat on waves below mountains and a rising sun"></div>
    <div class="company-name">Brantley Water Taxi &amp; Transport</div>
    <p class="captain"><span class="rank">Captain</span>Morgan Ellery</p>
    <ul class="contact-list">
      <li>
        <svg class="contact-icon" viewBox="0 0 17 17"><rect width="17" height="17" rx="3" fill="#3176b5"/><path d="M5 3.5c.6 0 1.7 2.3 1.4 2.8l-.9.9c.6 1.6 1.8 2.8 3.4 3.4l.9-.9c.5-.3 2.8.8 2.8 1.4 0 1-1 2-2 2C7 13 4 10 3.5 5.5c0-1 .6-2 1.5-2z" fill="#fff"/></svg>
        0224-555-0199
      </li>
      <li>
        <svg class="contact-icon" viewBox="0 0 17 17"><rect width="17" height="17" rx="3" fill="#3176b5"/><rect x="3" y="5" width="11" height="7.5" fill="none" stroke="#fff" stroke-width="1.2"/><path d="M3 5l5.5 4.5L14 5" fill="none" stroke="#fff" stroke-width="1.2"/></svg>
        morgan@brantleywatertaxi-example.com
      </li>
      <li>
        <svg class="contact-icon" viewBox="0 0 17 17"><rect width="17" height="17" rx="3" fill="#3176b5"/><circle cx="8.5" cy="8.5" r="5" fill="none" stroke="#fff" stroke-width="1.1"/><ellipse cx="8.5" cy="8.5" rx="2.2" ry="5" fill="none" stroke="#fff" stroke-width="1"/><path d="M3.5 8.5h10" stroke="#fff" stroke-width="1"/></svg>
        www.brantleywatertaxi-example.com
      </li>
    </ul>
    <div class="band-blue"></div>
    <div class="band-orange"></div>
  </section>

  <section class="card card-back">
    <div class="back-photo" role="img" aria-label="Blue-toned photograph of a landing-craft work boat moored at a dock"></div>
    <div class="back-name">Brantley Water Taxi &amp; Transport</div>
  </section>
</main>
</body>
</html>
```